Verran semiconductor corporate presentation

We need a new template with some fresh design elements as we've just announced the acquisition of a new company. Similarly, the backend of the ppt is not set up correctly - and doesn't format properly when dropping in copied text. Attached is the powerpoint presentation/ template as it stands today.
Industry/Entity Type
It Company
Font styles to use
Other font styles liked:
- Arial
Look and feel

```html
<!DOCTYPE html>
<html lang="en">
<head>
<meta charset="utf-8">
<title>Verran Semiconductor – Growth Markets</title>
<link rel="stylesheet" href="https://fonts.googleapis.com/css2?family=Arimo:wght@400&display=swap">
<style>
  :root {
    --title-blue: #1b5c9e;
    --arc-blue: #1d5fa3;
    --arc-light: #cfe3f3;
    --green: #9cc93d;
    --text-grey: #555a5e;
    --icon-dark: #34383c;
    --bg: #ffffff;
  }
  html, body { margin: 0; padding: 0; overflow: hidden; }
  body { width: 1200px; height: 831px; background: var(--bg); font-family: "Arimo", Arial, sans-serif; }
  .slide { position: relative; width: 1200px; height: 831px; overflow: hidden; background: var(--bg); }
  .backdrop { position: absolute; inset: 0 0 75px 0;
    background: radial-gradient(ellipse at 75% 40%, #f1f3f4 0%, #f7f8f8 45%, #ffffff 80%); }
  .title { position: absolute; left: 44px; top: 40px; margin: 0; font-weight: 400;
    font-size: 38px; line-height: 40px; color: var(--title-blue); }
  .subtitle { position: absolute; left: 46px; top: 188px; margin: 0; font-size: 23px; color: var(--text-grey); }
  .wave { position: absolute; left: 0; top: 0; }
  .label { position: absolute; width: 220px; margin-left: -110px; text-align: center;
    font-size: 24px; line-height: 34px; color: var(--text-grey); }
  .footer { position: absolute; left: 0; bottom: 0; width: 1200px; height: 75px; background: var(--green); }
  .footer-note { position: absolute; left: 0; width: 100%; top: 22px; text-align: center; font-size: 17px; color: #4a4f3a; }
  .page-num { position: absolute; right: 46px; top: 20px; font-size: 17px; color: #4a4f3a; }
</style>
</head>
<body>
<div class="slide">
  <div class="backdrop" role="img" aria-label="faint light grey circuit-board pattern background"></div>

  <h1 class="title">Focused on Growth<br>Markets and<br>Applications</h1>
  <p class="subtitle">Lowest power solutions available</p>

  <svg class="wave" width="1200" height="831" viewBox="0 0 1200 831">
    <defs>
      <linearGradient id="fadeDown" x1="0" y1="0" x2="0" y2="1">
        <stop offset="0" stop-color="#9cc93d"/>
        <stop offset="0.55" stop-color="#b6d872"/>
        <stop offset="1" stop-color="#9cc93d" stop-opacity="0"/>
      </linearGradient>
      <linearGradient id="fadeUp" x1="0" y1="1" x2="0" y2="0">
        <stop offset="0" stop-color="#9cc93d"/>
        <stop offset="0.55" stop-color="#b6d872"/>
        <stop offset="1" stop-color="#9cc93d" stop-opacity="0"/>
      </linearGradient>
    </defs>

    <!-- pillars rising from below -->
    <g fill="url(#fadeDown)">
      <path d="M96 482 A75 75 0 0 1 246 482 L246 756 L96 756 Z"/>
      <path d="M453 482 A75 75 0 0 1 603 482 L603 756 L453 756 Z"/>
      <path d="M810 482 A75 75 0 0 1 960 482 L960 756 L810 756 Z"/>
    </g>
    <!-- pillars hanging from above -->
    <g fill="url(#fadeUp)">
      <path d="M275 205 L425 205 L425 482 A75 75 0 0 1 275 482 Z"/>
      <path d="M632 205 L782 205 L782 482 A75 75 0 0 1 632 482 Z"/>
      <path d="M989 205 L1139 205 L1139 482 A75 75 0 0 1 989 482 Z"/>
    </g>

    <!-- wave line -->
    <path d="M82 482 A89 89 0 0 1 260 482 A89 89 0 0 0 439 482 A89 89 0 0 1 617 482 A89 89 0 0 0 796 482 A89 89 0 0 1 974 482 A89 89 0 0 0 1153 482"
          fill="none" stroke="var(--arc-blue)" stroke-width="13"/>
    <path d="M82 482 A89 89 0 0 1 260 482 A89 89 0 0 0 439 482 A89 89 0 0 1 617 482 A89 89 0 0 0 796 482 A89 89 0 0 1 974 482 A89 89 0 0 0 1153 482"
          fill="none" stroke="var(--arc-light)" stroke-width="2.5"/>

    <g fill="var(--icon-dark)">
      <!-- smartphone -->
      <rect x="145" y="432" width="52" height="106" rx="7"/>
      <rect x="151" y="444" width="40" height="78" fill="#9cc93d"/>
      <circle cx="171" cy="530" r="3" fill="#9cc93d"/>

      <!-- building -->
      <rect x="318" y="420" width="64" height="104"/>
      <rect x="332" y="410" width="6" height="12"/>
      <g fill="#b6d872">
        <rect x="326" y="430" width="11" height="11"/><rect x="344" y="430" width="11" height="11"/><rect x="362" y="430" width="11" height="11"/>
        <rect x="326" y="448" width="11" height="11"/><rect x="344" y="448" width="11" height="11"/><rect x="362" y="448" width="11" height="11"/>
        <rect x="326" y="466" width="11" height="11"/><rect x="344" y="466" width="11" height="11"/><rect x="362" y="466" width="11" height="11"/>
        <rect x="326" y="484" width="11" height="11"/><rect x="344" y="484" width="11" height="11"/><rect x="362" y="484" width="11" height="11"/>
        <rect x="340" y="505" width="8" height="19"/><rect x="352" y="505" width="8" height="19"/>
      </g>

      <!-- tyre -->
      <circle cx="527" cy="490" r="52"/>
      <circle cx="527" cy="490" r="33" fill="#b6d872"/>
      <circle cx="527" cy="490" r="11"/>
      <circle cx="527" cy="468" r="6"/><circle cx="548" cy="483" r="6"/><circle cx="540" cy="508" r="6"/>
      <circle cx="514" cy="508" r="6"/><circle cx="506" cy="483" r="6"/>

      <!-- headphones -->
      <path d="M655 502 L655 480 A51 51 0 0 1 757 480 L757 502 L746 502 L746 480 A40 40 0 0 0 666 480 L666 502 Z"/>
      <rect x="649" y="476" width="24" height="46" rx="6"/>
      <rect x="739" y="476" width="24" height="46" rx="6"/>

      <!-- watch -->
      <rect x="866" y="416" width="30" height="38" rx="4" transform="rotate(18 886 490)"/>
      <rect x="866" y="524" width="30" height="40" rx="4" transform="rotate(18 886 490)"/>
      <circle cx="886" cy="490" r="33"/>
      <circle cx="886" cy="490" r="25" fill="#b6d872"/>
      <path d="M886 472 L886 490 L896 506" fill="none" stroke="var(--icon-dark)" stroke-width="3"/>

      <!-- TV -->
      <rect x="1002" y="430" width="124" height="72" rx="3"/>
      <rect x="1011" y="438" width="106" height="56" fill="#b6d872"/>
      <rect x="1056" y="502" width="16" height="8"/>
      <rect x="1038" y="509" width="52" height="6" rx="2"/>
    </g>
  </svg>

  <div class="label" style="left:171px; top:604px;">Smartphones<br>Tablets</div>
  <div class="label" style="left:350px; top:266px;">Smart Buildings<br>Beacons</div>
  <div class="label" style="left:528px; top:604px;">Auto</div>
  <div class="label" style="left:707px; top:266px;">Headphones<br>Headsets<br>Mics</div>
  <div class="label" style="left:886px; top:604px;">Wearables<br>Smart Tags</div>
  <div class="label" style="left:1064px; top:266px;">Smart TV<br>Set Top Box</div>

  <footer class="footer">
    <div class="footer-note">© 2017 Verran Semiconductor</div>
    <div class="page-num">7</div>
  </footer>
</div>
</body>
</html>
```